Business Card Design

I need a Business Card that will catch the attention that will not get thrown in a Drawer. I have 23 companies I use for Auto, Home, Life, and Business Insurance. I make sure that people have the best coverage for the $ spent.

Industry/Entity Type

Business

Contact Information for Business Card

Dorlin Insurance Agency, Inc., Marcus Helgren, 4375 West Tamber Lane Larkmoor, Avela 45192 555-281-7496, www.dorlinagency.example, Friendly, Linkora, Circlo

```html
<!DOCTYPE html>
<html lang="en">
<head>
<meta charset="utf-8">
<title>Dorlin Insurance Agency – Business Card</title>
<link rel="stylesheet" href="https://fonts.googleapis.com/css2?family=Cinzel:wght@700&family=Della+Respira&display=swap">
<style>
  :root {
    --page: #ffffff;
    --frame-red: #d0302a;
    --frame-cyan: #12a9e0;
    --navy-deep: #0a3356;
    --navy-mid: #437ca4;
    --band-blue: #6d9fd6;
    --ink: #111111;
    --logo-ink: #2b2b2b;
    --link-blue: #5b8ac4;
    --chip: #ffffff;
  }
  html, body {
    margin: 0;
    padding: 0;
    width: 1200px;
    height: 704px;
    overflow: hidden;
    background: var(--page);
  }
  .card {
    position: relative;
    width: 1200px;
    height: 704px;
    font-family: "Della Respira", Georgia, serif;
    color: var(--ink);
  }
  .card__frame {
    position: absolute;
    inset: 0;
  }
  .card__field {
    position: absolute;
    left: 47px;
    top: 45px;
    width: 1109px;
    height: 610px;
    background: linear-gradient(
      to bottom,
      var(--navy-deep) 0%,
      var(--navy-deep) 15%,
      var(--navy-mid) 58%,
      var(--navy-deep) 86%,
      var(--navy-deep) 100%
    );
  }
  .card__top-rule {
    position: absolute;
    left: 51px;
    top: 50px;
    width: 1100px;
    height: 2px;
    background: var(--band-blue);
  }
  .card__band {
    position: absolute;
    background: var(--band-blue);
  }
  .card__band--top { left: 51px; top: 91px; width: 1101px; height: 29px; }
  .card__band--bottom { left: 55px; top: 633px; width: 1089px; height: 21px; }
  .card__divider {
    position: absolute;
    left: 556px;
    top: 229px;
    width: 3px;
    height: 372px;
    background: var(--ink);
  }
  .brand {
    position: absolute;
    left: 183px;
    top: 280px;
    width: 300px;
    text-align: center;
    font-family: "Cinzel", Georgia, serif;
    font-weight: 700;
    color: var(--logo-ink);
    line-height: 1;
  }
  .brand__name { font-size: 52px; letter-spacing: 1px; }
  .brand__line { font-size: 27px; margin-top: 6px; }
  .brand__line--small { font-size: 24px; margin-top: 4px; letter-spacing: 1px; }
  .contact {
    position: absolute;
    left: 582px;
    top: 246px;
    font-size: 28px;
    line-height: 37px;
    margin: 0;
    font-style: normal;
  }
  .contact__name { padding-left: 5px; }
  .web {
    position: absolute;
    left: 790px;
    top: 497px;
    display: flex;
    align-items: center;
    gap: 16px;
  }
  .web__label { font-size: 14px; }
  .web__link {
    display: block;
    width: 268px;
    height: 33px;
    line-height: 33px;
    text-align: center;
    background: var(--chip);
    border-radius: 16px;
    color: var(--link-blue);
    font-size: 19px;
    text-decoration: none;
  }
  .social {
    position: absolute;
    left: 872px;
    top: 566px;
    display: flex;
    gap: 8px;
    margin: 0;
    padding: 0;
    list-style: none;
  }
  .social__item {
    width: 68px;
    height: 36px;
    line-height: 36px;
    text-align: center;
    background: var(--chip);
    border-radius: 6px;
    font-size: 14px;
    color: var(--navy-deep);
  }
</style>
</head>
<body>
<main class="card">
  <svg class="card__frame" width="1200" height="704" viewBox="0 0 1200 704" aria-hidden="true">
    <rect x="22" y="20" width="1160" height="660" fill="none" stroke="var(--frame-red)" stroke-width="4"/>
    <rect x="45" y="43" width="1113" height="614" fill="none" stroke="var(--frame-cyan)" stroke-width="6"/>
  </svg>
  <div class="card__field"></div>
  <div class="card__top-rule"></div>
  <div class="card__band card__band--top"></div>
  <div class="card__band card__band--bottom"></div>

  <div class="brand">
    <div class="brand__name">DORLIN</div>
    <div class="brand__line">INSURANCE</div>
    <div class="brand__line brand__line--small">AGENCY</div>
  </div>

  <div class="card__divider"></div>

  <address class="contact">
    <div class="contact__name">Marcus Helgren,</div>
    <div>4375 West Tamber Lane Larkmoor,</div>
    <div>Avela 45192 555-281-7496</div>
  </address>

  <div class="web">
    <span class="web__label">email:-</span>
    <a class="web__link" href="#">www.dorlinagency.example</a>
  </div>

  <ul class="social">
    <li class="social__item">Friendly</li>
    <li class="social__item">Circlo</li>
    <li class="social__item">Linkora</li>
  </ul>
</main>
</body>
</html>
```